K & D A/C Compressors' Business Card

Hello,

I need someone to create a new business card for my business. The name of my Business is: K & D A/C Compressors. I sell automotive air conditioning parts (a/c parts). I would like the business card to incorporate my logo, and to have an automotive feel to it. It is important that the business card feel like it is coming from an automotive parts business.

I already have a logo, which I will provide.

Thanks.

Project Deadline Extended Reason: I feel like extending the deadline until October 9, 2017, will allow for more time to design the business card. Thank you for your understanding. Added Monday, October 2, 2017

Target Market(s)

Consumers who need automotive a/c parts, and auto mechanics.

Industry/Entity Type

Automotive

Contact Information for Business Card

Business name: K & D A/C Compressors
Business Address: 48207 Southwest 64th Avenue, North Miami Beach, Florida 33847
Telephone: 305-642-1730
Fax: To be provided once I choose your design.
Website: www.kdcoolparts.example
Email: support@kdcoolparts.example
Names: To be provided once I choose your design.

Font styles to use
Sans Serif

Colors

Designer to choose colors to be used in the design.

Requirements
Must have
• The business card must include all of the "Business Card Details" and the logo I have uploaded.

```html
<!DOCTYPE html>
<html lang="en">
<head>
<meta charset="utf-8">
<title>K &amp; D A/C Compressors – Business Card</title>
<link rel="stylesheet" href="https://fonts.googleapis.com/css2?family=Open+Sans:wght@300;400;600;700&display=swap">
<style>
  :root {
    --backdrop: #5a4a3e;
    --card: #f4f4f4;
    --brand-blue: #05b4ee;
    --brand-grey: #9b9c9e;
    --ink: #333638;
    --muted: #a4a5a7;
    --white: #ffffff;
  }
  * { margin: 0; padding: 0; box-sizing: border-box; }
  html, body {
    width: 1200px; height: 886px; overflow: hidden;
    background: var(--backdrop);
    font-family: "Open Sans", Arial, sans-serif;
  }
  .stage {
    width: 1200px; height: 886px;
    display: flex; flex-direction: column; align-items: center; justify-content: center;
    gap: 34px;
  }
  .card {
    position: relative;
    width: 700px; height: 400px;
    background: var(--card);
    border-radius: 26px;
    overflow: hidden;
    box-shadow: 0 10px 24px rgba(0,0,0,.35);
  }

  /* Front */
  .card-front { display: flex; flex-direction: column; align-items: center; justify-content: center; }
  .brand { display: flex; align-items: center; gap: 18px; }
  .brand-mark { width: 46px; height: 46px; background: var(--brand-blue); }
  .brand-name {
    color: var(--brand-grey); font-weight: 600; line-height: 1.05;
    display: flex; flex-direction: column;
  }
  .brand-name .initials { font-size: 62px; letter-spacing: 2px; }
  .brand-name .trade { font-size: 34px; }
  .front-web {
    margin-top: 26px; font-size: 15px; letter-spacing: 6px; color: var(--ink);
    margin-left: 60px;
  }

  /* Back */
  .band { position: absolute; inset: 0; }
  .back-brand {
    position: absolute; left: 44px; bottom: 40px;
    color: var(--white); font-weight: 600; line-height: 1.1;
    display: flex; flex-direction: column;
  }
  .back-brand .initials { font-size: 44px; letter-spacing: 2px; }
  .back-brand .trade { font-size: 24px; }
  .contact {
    position: absolute; left: 370px; top: 40px;
    font-size: 15px; color: var(--ink); line-height: 1.35;
  }
  .person-name { color: var(--brand-blue); font-size: 22px; font-weight: 600; }
  .person-role { color: var(--muted); font-size: 14px; letter-spacing: 1px; margin-bottom: 8px; }
  .label { color: var(--brand-blue); font-weight: 700; }
  .divider { width: 40px; height: 2px; background: var(--brand-blue); margin: 9px 0; }
</style>
</head>
<body>
<main class="stage">
  <section class="card card-front" aria-label="Business card front">
    <div class="brand">
      <span class="brand-mark"></span>
      <p class="brand-name"><span class="initials">K &amp; D</span><span class="trade">A/C Compressors</span></p>
    </div>
    <p class="front-web">www.kdcoolparts.example</p>
  </section>

  <section class="card card-back" aria-label="Business card back">
    <svg class="band" width="700" height="400" viewBox="0 0 700 400" aria-hidden="true">
      <polygon points="0,170 700,360 700,400 0,400" fill="var(--brand-blue)"/>
    </svg>
    <p class="back-brand"><span class="initials">K &amp; D</span><span class="trade">A/C Compressors</span></p>
    <div class="contact">
      <p class="person-name">ALEX MORENO</p>
      <p class="person-role">CEO/FOUNDER</p>
      <p><span class="label">P:</span>305-642-1730</p>
      <p><span class="label">F:</span>305-642-1731</p>
      <div class="divider"></div>
      <p>48207 Southwest 64th Avenue<br>North Miami Beach,<br>Florida 33847</p>
      <div class="divider"></div>
      <p><span class="label">W:</span>www.kdcoolparts.example</p>
      <p><span class="label">E:</span>support@kdcoolparts.example</p>
    </div>
  </section>
</main>
</body>
</html>
```